Modern Business Card

Modern professional business card with more than just logo and demographic info. Something memorable.

We are a trendy/modern chiropractic group with an emphasis on neurology, hence the minimalist-type brain logo. We want to convey that modern and technical aspect with professionalism and the elite nature of our practice environment.

```html
<!DOCTYPE html>
<html lang="en">
<head>
<meta charset="utf-8">
<title>Meridian Spine Care – Business Card</title>
<link rel="stylesheet" href="https://fonts.googleapis.com/css2?family=Marcellus&family=Lora:wght@400&family=Saira+Semi+Condensed:wght@600&display=swap">
<style>
  :root {
    --backdrop: #e4ddd5;
    --card: #eef0f1;
    --card-edge: #c9cdd0;
    --ink: #2b2625;
    --ink-soft: #3f3a39;
    --accent: #3f5f98;
  }
  * { margin: 0; padding: 0; box-sizing: border-box; }
  html, body {
    width: 1200px; height: 1054px; overflow: hidden;
    background: var(--backdrop);
  }
  .card {
    position: absolute; left: 150px; top: 270px;
    width: 900px; height: 514px;
    background: var(--card);
    border: 1px solid var(--card-edge);
    border-radius: 3px;
    box-shadow: 0 10px 30px rgba(0,0,0,0.12);
    color: var(--ink);
  }
  .wordmark { position: absolute; left: 55px; top: 50px; font-family: "Marcellus", serif; line-height: 1; }
  .wordmark__main { font-size: 64px; letter-spacing: 1px; color: #151212; }
  .wordmark__sub { font-size: 36px; letter-spacing: 1px; color: var(--ink-soft); margin-top: 2px; }
  .person { position: absolute; left: 55px; top: 222px; }
  .person__name { font-family: "Saira Semi Condensed", sans-serif; font-weight: 600; font-size: 36px; color: var(--accent); line-height: 1.1; }
  .person__title { font-family: "Lora", serif; font-size: 21px; color: var(--ink-soft); margin-top: 8px; }
  .contacts { position: absolute; left: 55px; top: 330px; list-style: none; font-family: "Lora", serif; font-size: 21px; color: var(--ink-soft); }
  .contacts li { display: flex; align-items: center; height: 33px; }
  .contacts svg { width: 20px; height: 20px; margin-right: 19px; fill: var(--accent); }
  .address { position: absolute; left: 55px; top: 438px; font-family: "Lora", serif; font-size: 21px; line-height: 33px; color: var(--ink-soft); }
  .brand-mark { position: absolute; left: 505px; top: 0; width: 395px; height: 514px; display: flex; align-items: center; justify-content: center; gap: 18px; }
  .brand-mark__dot { width: 46px; height: 46px; border-radius: 50%; background: var(--accent); }
  .brand-mark__name { font-family: "Lora", serif; font-size: 42px; color: var(--accent); }
</style>
</head>
<body>
  <article class="card">
    <header class="wordmark">
      <div class="wordmark__main">MERIDIAN</div>
      <div class="wordmark__sub">SPINE CARE</div>
    </header>

    <div class="person">
      <div class="person__name">Alex Ray Turner</div>
      <div class="person__title">Managing Director</div>
    </div>

    <ul class="contacts">
      <li>
        <svg viewBox="0 0 20 20" aria-hidden="true"><path d="M2 6c0-2 3-3 8-3s8 1 8 3v2h-4V6.5c-1-.6-6-.6-8 0V8H2z"/><path d="M5 9h10l2 8H3z"/></svg>
        555-240-7788
      </li>
      <li>
        <svg viewBox="0 0 20 20" aria-hidden="true"><path d="M2 4h16v12H2z" fill="none" stroke="#3f5f98" stroke-width="2"/><path d="M2 4l8 7 8-7" fill="none" stroke="#3f5f98" stroke-width="2"/></svg>
        alex@meridianspinecare.com
      </li>
      <li>
        <svg viewBox="0 0 20 20" aria-hidden="true"><circle cx="10" cy="10" r="8" fill="none" stroke="#3f5f98" stroke-width="2"/><path d="M2 10h16M10 2c3 3 3 13 0 16M10 2c-3 3-3 13 0 16" fill="none" stroke="#3f5f98" stroke-width="1.5"/></svg>
        www.meridianspinecare.com
      </li>
    </ul>

    <address class="address" style="font-style:normal">
      87 Sample Rd., Lakeview,<br>
      Fairfield, US 204518
    </address>

    <div class="brand-mark">
      <span class="brand-mark__dot"></span>
      <span class="brand-mark__name">Meridian</span>
    </div>
  </article>
</body>
</html>
```